The Suds Lounge Website | ||
Cleaning | ||
thesudslounge.example | ||
The Suds Lounge is an upscale, technologically advanced laundromat providing customers with free wifi, the most efficient washers and dryers, cafe seating with coffee and other snacks and beverages in a comfortable environment. | ||
Likes: Dimensional and visually engaging. Clean and intuitive. Polished. Reinforced branding. Creative nav button presentation. Dislikes: Super Linear, boring, and cluttered. |
Cutting-Edge Unique/Creative Friendly Modern Elegant Progressive Fun |
Rich Teal (See Logo) | ||
Rich Gold (See Logo) | ||
below header | ||
While most customers are women, the site should not be overly femine, so that both sexes will feel that the site is made for them. Main sections: header, nav (Home, About Us, Services, Customer Voice, Just For You, Contact Us), main content and side bar for highlights. The site will include video testimonials from customers and photos. We want customers to be able to take a tour through the store. We are trying to engage customers to Preorder their TSL Rinse Pass and receive an extra $3.00 FREE! We are asking customers to "Like Us" on friendnest, follow us on chirpline and review us on ratespot!. Using the associated icons. The design should reflect two locations. Maple and Birch Court (Directly across from Grocer Vale) Phone: 555-907-3318 Hours: 7a – 11p Monday - Sunday Harborlight Commons Juniper and 9 Ave. Phone: 555-907-3318 Hours: 7a – 11p Monday - Sunday |

```html
<!DOCTYPE html>
<html lang="en">
<head>
<meta charset="utf-8">
<title>The Suds Lounge</title>
<link rel="stylesheet" href="https://fonts.googleapis.com/css2?family=Oswald:wght@400;600&family=Open+Sans:wght@400;600;700&display=swap">
<style>
:root{
  --teal:#1d7f94;
  --teal-dark:#0f5f72;
  --gold:#c79a2c;
  --gold-dark:#8e6a16;
  --ink:#3a3a3a;
  --muted:#6b6b6b;
  --page:#ffffff;
  --bg:#e3e6e8;
  --rule:#d6dadc;
}
*{margin:0;padding:0;box-sizing:border-box}
html,body{width:1200px;height:886px;overflow:hidden}
body{background:linear-gradient(#eef0f1,var(--bg));font-family:"Open Sans",Arial,sans-serif;color:var(--ink);position:relative}
.page{position:absolute;left:160px;top:0;width:880px;height:886px;background:var(--page);box-shadow:0 0 14px rgba(0,0,0,.15)}
.abs{position:absolute}

/* header */
.brand{left:30px;top:14px;display:flex;align-items:center;gap:10px}
.brand-name{font-family:"Oswald",sans-serif;font-weight:600;font-size:30px;line-height:1;color:var(--teal);width:140px}
.brand-dot{width:62px;height:62px;border-radius:50%;background:var(--teal)}
.tagline{left:168px;top:82px;font-size:11px;color:var(--teal);font-style:italic}
.promo{left:430px;top:8px;width:210px;height:100px}
.promo-text{position:absolute;left:0;top:0;width:210px;height:100px;display:flex;flex-direction:column;justify-content:center;align-items:center;transform:rotate(-6deg);color:#fff;font-family:"Oswald",sans-serif;text-transform:uppercase;line-height:1.05}
.promo-big{font-size:22px;font-weight:600;display:flex;align-items:center;gap:4px}
.promo-big b{font-size:40px}
.promo-small{font-size:11px;letter-spacing:.5px}
.social{right:62px;top:10px;display:flex;gap:8px}
.social span{display:flex;align-items:center;gap:3px;font-size:9px;color:var(--teal-dark);font-weight:600}
.social i{display:block;width:14px;height:14px;background:var(--teal)}
.phone-top{right:40px;top:76px;display:flex;align-items:center;gap:6px;font-family:"Oswald",sans-serif;font-size:22px;color:var(--teal-dark);font-weight:600}

/* nav */
.nav{left:0;top:115px;width:880px;height:34px;background:linear-gradient(var(--teal),var(--teal-dark));display:flex;align-items:center;padding-left:122px;gap:0}
.nav a{color:#fff;text-decoration:none;font-size:12px;font-weight:600;text-transform:uppercase;padding:0 21px;border-right:1px solid rgba(255,255,255,.35);line-height:14px}
.nav a:last-child{border-right:0}

/* slider */
.slider{left:25px;top:160px;width:830px;height:224px;background:linear-gradient(180deg,#cfd8dc 0%,#9eaab0 45%,#b9c3c7 100%);box-shadow:0 4px 8px rgba(0,0,0,.2)}
.dots{left:42px;top:362px;display:flex;gap:6px}
.dots i{width:10px;height:10px;background:#9aa4a8;display:block}
.dots i:first-child{background:var(--gold)}

/* columns */
.col{top:418px;height:300px}
.col-about{left:20px;width:264px}
.col-reasons{left:296px;width:276px;border-left:1px solid var(--rule);border-right:1px solid var(--rule);padding:0 12px}
.col-voice{left:588px;width:276px}
.col-title{display:flex;align-items:center;gap:6px;font-family:"Oswald",sans-serif;font-size:18px;color:var(--teal-dark);text-transform:uppercase;height:36px;margin-bottom:8px}
.col-title::before{content:"";width:26px;height:26px;border:3px solid var(--teal);border-right-color:transparent;border-radius:50%}
.col p{font-size:12px;line-height:16px;color:var(--ink)}
.reasons{list-style:none}
.reasons li{font-size:11.5px;font-weight:600;display:flex;align-items:center;gap:10px;height:21.5px}
.reasons li::before{content:"";width:11px;height:11px;border:2px solid var(--gold);border-radius:50%}
.video{position:relative;height:110px;margin-bottom:8px;display:flex;align-items:center;justify-content:center}
.video-a{background:linear-gradient(90deg,#e9ecee,#c8ced2)}
.video-b{background:linear-gradient(90deg,#d9dde0,#a9b1b6)}
.play{width:48px;height:48px}
.more{position:absolute;right:0;bottom:0;font-size:11px;font-weight:700;color:var(--teal-dark);text-decoration:underline}
.col-reasons .more{right:12px}

/* locations */
.locations{left:20px;top:758px;width:840px;height:70px;border-top:1px solid var(--rule);padding-top:14px}
.loc-title{left:0;top:16px;display:flex;align-items:center;gap:6px;font-family:"Oswald",sans-serif;font-size:18px;color:var(--teal-dark);text-transform:uppercase}
.loc-title::before{content:"";width:26px;height:26px;border:3px solid var(--teal);border-right-color:transparent;border-radius:50%}
.loc{top:20px;font-size:11px;color:var(--muted);line-height:15px}
.loc strong{display:block;font-family:"Oswald",sans-serif;font-weight:400;font-size:16px;color:var(--teal-dark);line-height:20px}
.loc-hours{top:22px;left:594px;font-size:11px;line-height:15px}

/* footer */
.footer{left:0;top:842px;width:880px;height:28px;background:linear-gradient(var(--teal),var(--teal-dark));color:#fff;font-size:11px;display:flex;align-items:center;justify-content:center}
</style>
</head>
<body>
<div class="page">
  <header>
    <div class="abs brand"><div class="brand-name">The Suds Lounge</div><div class="brand-dot"></div></div>
    <div class="abs tagline">Experience Clean!</div>

    <div class="abs promo">
      <svg width="210" height="100" viewBox="0 0 210 100">
        <polygon points="8,18 200,0 206,80 14,100" fill="#8e6a16"/>
        <polygon points="4,14 196,-2 202,76 10,96" fill="#c79a2c"/>
      </svg>
      <div class="promo-text">
        <div class="promo-big">Get Extra <b>$3</b></div>
        <div class="promo-small">On preorder</div>
        <div class="promo-small">TSL Rinse Pass</div>
      </div>
    </div>

    <div class="abs social">
      <span><i></i>friendnest</span>
      <span><i></i>chirpline</span>
      <span><i></i>ratespot</span>
    </div>

    <div class="abs phone-top">
      <svg width="22" height="16" viewBox="0 0 22 16"><path d="M2 6c0-3 4-5 9-5s9 2 9 5l-4 1-1-3H7L6 7z" fill="#0f5f72"/><rect x="5" y="8" width="12" height="7" rx="2" fill="#0f5f72"/></svg>
      555-907-3318
    </div>
  </header>

  <nav class="abs nav">
    <a href="#">Home</a><a href="#">About Us</a><a href="#">Services</a><a href="#">Customer Voice</a><a href="#">Just For You</a><a href="#">Contact Us</a>
  </nav>

  <div class="abs slider" role="img" aria-label="Photo of a row of front-loading washers in the laundromat"></div>
  <div class="abs dots"><i></i><i></i><i></i><i></i></div>

  <section class="abs col col-about">
    <h2 class="col-title">Welcome to The Suds Lounge</h2>
    <p>The Suds Lounge is an upscale, technologically advanced Laundromat providing customers with free wifi, the most efficient washers and dryers, cafe seating with coffee and other snacks and beverages in a comfortable environment. The Suds Lounge is an upscale, technologically advanced Laundromat providing customers with free wifi, the most efficient washers and dryers, cafe seating with coffee and other snacks and beverages in a comfortable environment. The Suds Lounge is an upscale, technologically advanced Laundromat providing...</p>
    <a class="more" href="#">Read more...</a>
  </section>

  <section class="abs col col-reasons">
    <h2 class="col-title">Top 10 reasons to choose us</h2>
    <ul class="reasons">
      <li>Variety of hot and iced drinks</li>
      <li>Sandwiches, wraps, snacks</li>
      <li>Free Wi Fi</li>
      <li>Computers on site</li>
      <li>Variety of hot and iced drinks</li>
      <li>Sandwiches, wraps, snacks</li>
      <li>Free Wi Fi</li>
      <li>Computers on site</li>
      <li>Variety of hot and iced drinks</li>
      <li>Sandwiches, wraps, snacks</li>
    </ul>
    <a class="more" href="#">Read more...</a>
  </section>

  <section class="abs col col-voice">
    <h2 class="col-title">Why people choose us</h2>
    <div class="video video-a" role="img" aria-label="Video testimonial from a customer">
      <svg class="play" viewBox="0 0 48 48"><circle cx="24" cy="24" r="23" fill="#1d7f94"/><polygon points="19,14 35,24 19,34" fill="#fff"/></svg>
    </div>
    <div class="video video-b" role="img" aria-label="Video testimonial from a customer">
      <svg class="play" viewBox="0 0 48 48"><circle cx="24" cy="24" r="23" fill="#1d7f94"/><polygon points="19,14 35,24 19,34" fill="#fff"/></svg>
    </div>
    <a class="more" href="#">Read more...</a>
  </section>

  <section class="abs locations">
    <h2 class="abs loc-title">Our Locations</h2>
    <div class="abs loc" style="left:168px"><strong>Maple and Birch Court</strong>(Directly across from Grocer Vale)</div>
    <div class="abs loc" style="left:396px"><strong>Harborlight Commons</strong>Juniper and 9 Ave.</div>
    <div class="abs loc-hours"><b>Phone:</b> 555-907-3318<br>Monday – Sunday<br>7:00am – 11:00pm</div>
  </section>

  <footer class="abs footer">The Suds Lounge © 2011</footer>
</div>
</body>
</html>
```